New Business Card Design Project - RK Ledgerwise & Filing Partners, LLC

Below is a sample image of the card (TM Bookkeeping). I would like to have a designed business card that looks very similar (Front & Back). In addition, I would like to keep the same colors as well. I attached my Business Logo (RK Ledgerwise & Filing Partners, LLC) that will be on my website.

Target Market(s)

Executives, Business Owners, Board of Directors, Chief Financial Officers

Contact Information for Business Card

Font styles to use
Serif

Colors
0c5ba6
ffffff
5c5c5c

Requirements
Must have
• My Name: Malcolm Ferris, CPA
• Position: Owner
• Phone: (240) 555-0148
• Email: Mferris@rkledgerwise.example
• Website: www.Rkledgerwise.example
• Address: 4736 Ferncliff Ave #2093
• Dunmore Falls, MD 21990
Nice to have
• Same design & color scheme as TM Bookkeepnig Business card sample attached

```html
<!DOCTYPE html>
<html lang="en">
<head>
<meta charset="utf-8">
<title>RK Ledgerwise &amp; Filing Partners – Business Card</title>
<link rel="stylesheet" href="https://fonts.googleapis.com/css2?family=Tinos:ital,wght@0,400;1,700&display=swap">
<style>
  :root {
    --brand-blue: #14b1e0;
    --brand-grey: #6b6969;
    --text-grey: #666666;
    --paper: #ffffff;
    --stage: #3c3c3c;
  }
  * { margin: 0; padding: 0; box-sizing: border-box; }
  html, body { width: 1200px; height: 999px; overflow: hidden; }
  body {
    position: relative;
    background: var(--stage);
    font-family: "Tinos", "Times New Roman", serif;
  }
  .card {
    position: absolute;
    left: 220px;
    width: 760px;
    height: 434px;
    overflow: hidden;
  }
  .card--front { top: 60px; background: var(--paper); }
  .card--back { top: 532px; background: var(--brand-blue); }

  .brand {
    position: absolute;
    display: flex;
    align-items: center;
    white-space: nowrap;
  }
  .brand__mark { width: 34px; height: 34px; flex: none; margin-right: 18px; }
  .brand__name { font-size: 27px; letter-spacing: 1.2px; font-weight: 400; }
  .card--front .brand { left: 48px; top: 70px; }
  .card--front .brand__mark { background: var(--brand-blue); }
  .card--front .brand__name { color: var(--brand-blue); }
  .card--back .brand { left: 88px; top: 194px; }
  .card--back .brand__mark { background: var(--paper); }
  .card--back .brand__name { color: var(--paper); }

  .person { position: absolute; left: 44px; top: 308px; }
  .person__name {
    color: var(--brand-blue);
    font-style: italic;
    font-weight: 700;
    font-size: 22px;
    line-height: 26px;
  }
  .person__role { color: var(--text-grey); font-size: 16px; margin-top: 5px; }

  .address {
    position: absolute;
    left: 448px;
    top: 214px;
    color: var(--text-grey);
    font-size: 17px;
    line-height: 21px;
    font-style: normal;
  }
  .contact-list { position: absolute; left: 448px; top: 280px; list-style: none; }
  .contact-list li {
    display: flex;
    align-items: center;
    height: 28.5px;
    color: var(--text-grey);
    font-size: 17px;
  }
  .contact-list svg { width: 18px; height: 18px; margin-right: 19px; flex: none; }

  .footer-band { position: absolute; left: 0; bottom: 0; width: 760px; height: 56px; }
</style>
</head>
<body>
  <section class="card card--front" aria-label="Card front">
    <div class="brand">
      <span class="brand__mark"></span>
      <span class="brand__name">RK LEDGERWISE &amp; FILING PARTNERS</span>
    </div>

    <address class="address">4736 Ferncliff Ave #2093<br>Dunmore Falls, MD 21990</address>

    <ul class="contact-list">
      <li>
        <svg viewBox="0 0 18 18" aria-hidden="true">
          <rect width="18" height="18" rx="3" fill="#14b1e0"/>
          <path d="M6 3.5c-1.5.5-2 1.8-1.6 3.4.8 3.2 3.3 6 6.3 7.2 1.5.6 2.8.1 3.5-1.2l-2.2-1.8-1.4 1c-1.6-.8-3-2.4-3.6-4l1.2-1.2L6 3.5z" fill="#fff"/>
        </svg>
        (240) 555-0148
      </li>
      <li>
        <svg viewBox="0 0 18 18" aria-hidden="true">
          <path d="M1 7 9 1l8 6v10H1z" fill="#14b1e0"/>
          <rect x="4" y="5" width="10" height="6" fill="#fff"/>
          <path d="M1 7l8 6 8-6" fill="none" stroke="#fff" stroke-width="1.4"/>
        </svg>
        Mferris@rkledgerwise.example
      </li>
      <li>
        <svg viewBox="0 0 18 18" aria-hidden="true">
          <path d="M7 1.5c.8 0 1.4.6 1.4 1.4V8l4.6 1c1.2.3 1.8 1.2 1.6 2.4L14 17H7.2L3.4 11.5c-.5-.7-.2-1.5.6-1.7.5-.1 1 .1 1.3.5l.3.5V2.9c0-.8.6-1.4 1.4-1.4z" fill="#14b1e0"/>
        </svg>
        www.Rkledgerwise.example
      </li>
    </ul>

    <div class="person">
      <p class="person__name">Malcolm Ferris, CPA</p>
      <p class="person__role">Owner</p>
    </div>

    <svg class="footer-band" viewBox="0 0 760 56" aria-hidden="true">
      <rect x="0" y="17" width="400" height="39" fill="var(--brand-grey)"/>
      <polygon points="406,0 760,0 760,56 364,56" fill="var(--brand-blue)"/>
    </svg>
  </section>

  <section class="card card--back" aria-label="Card back">
    <div class="brand">
      <span class="brand__mark"></span>
      <span class="brand__name">RK LEDGERWISE &amp; FILING PARTNERS</span>
    </div>
  </section>
</body>
</html>
```